Technology Charity needs a Web Design

Velmo Puna purchases used company mobiles and donates the proceeds to charity. It is showing companies how they can do social good, with unused technology. We would like to see designs with relevant images of social good. Open to ideas, and more is explained in the attached brief. Logo is attached as well.

```html
<!DOCTYPE html>
<html lang="en">
<head>
<meta charset="utf-8">
<title>Velmo Puna — Mission</title>
<link href="https://fonts.googleapis.com/css2?family=Mulish:wght@400;600&family=Poppins:wght@600;700&family=Playfair+Display:wght@800;900&family=Roboto:wght@300;400;500&display=swap" rel="stylesheet">
<style>
:root{
  --sage:#8eaeb6;
  --sage-dark:#7f9ea7;
  --navy:#2b2d5b;
  --ink:#1c1c1c;
  --link:#7aa0b0;
  --white:#ffffff;
  --accent:#f06b3a;
}
*{margin:0;padding:0;box-sizing:border-box}
html,body{width:1200px;height:3310px;overflow:hidden;background:var(--white)}
body{position:relative;font-family:'Roboto',sans-serif;color:var(--ink)}
.abs{position:absolute}

.topbar{left:0;top:0;width:1200px;height:53px;font-family:'Mulish',sans-serif;font-size:14px;color:#333}
.topbar .notice{position:absolute;left:329px;top:18px}
.topbar .notice span{color:var(--link)}
.topbar .follow{position:absolute;left:958px;top:18px;display:flex;align-items:center;gap:10px}
.topbar .dot{width:10px;height:10px;border-radius:50%;background:var(--navy)}

.nav{left:0;top:53px;width:1200px;height:88px;background:var(--sage)}
.brand{position:absolute;left:99px;top:0;width:200px;height:88px;background:var(--white);display:flex;align-items:center;justify-content:center}
.wordmark{font-family:'Roboto',sans-serif;font-size:20px;font-weight:500;color:var(--navy);line-height:1}
.menu{position:absolute;top:26px;font-family:'Mulish',sans-serif;color:var(--white)}
.menu .num{font-size:11px;display:block;margin-bottom:4px}
.menu .lbl{font-size:15px}
.search{position:absolute;left:1096px;top:28px;width:32px;height:32px;border:1.5px solid #b7c9d2;border-radius:50%}
.search svg{position:absolute;left:9px;top:9px}

.hero{left:0;top:141px;width:1200px;height:626px;background:linear-gradient(120deg,#5a5048 0%,#8a7a6e 35%,#6e6660 60%,#3e4a5a 100%)}
.hero h1{position:absolute;left:0;width:1200px;top:310px;text-align:center;font-family:'Poppins',sans-serif;font-weight:700;font-size:58px;color:var(--white)}
.hero .btn{position:absolute;left:528px;top:450px;width:145px;height:48px;border-radius:24px;background:var(--sage);color:var(--white);font-family:'Mulish',sans-serif;font-size:15px;display:flex;align-items:center;justify-content:center}
.hero .arrow{position:absolute;top:358px}

.section-title{left:0;width:1200px;top:862px;text-align:center;font-family:'Playfair Display',serif;font-weight:900;font-size:48px;color:var(--navy)}
.photo{background:#ddd}
.framed{border:2px solid var(--sage);background:linear-gradient(180deg,#fafafa,#eceff0)}
.copy{font-size:20.5px;line-height:29.2px;font-weight:400;color:var(--ink);width:478px}
.closing{left:100px;width:1000px;top:2733px;text-align:center;font-size:24px;font-weight:500;line-height:30px}

.footer{left:0;top:2828px;width:1200px;height:399px;background:var(--sage);color:var(--white);font-family:'Mulish',sans-serif}
.footer h3{font-family:'Playfair Display',serif;font-weight:800;font-size:18px;margin-bottom:26px}
.col{position:absolute;top:102px}
.col li{list-style:none;font-size:15px;margin-bottom:13px}
.contact .lab{font-size:13px;display:flex;align-items:center;gap:8px;margin-bottom:8px}
.contact .val{font-size:13px;line-height:22px;margin-bottom:14px}
.news{display:flex;gap:20px;margin-bottom:32px}
.news .thumb{width:77px;height:64px;border-radius:3px;flex:none}
.news .txt{border-left:1px dashed #d6e2e6;padding-left:20px;font-size:15px;line-height:22px}
.news .meta{font-size:13px;margin-top:4px;display:flex;align-items:center;gap:6px}
.news .meta i{width:7px;height:7px;border-radius:50%;background:var(--accent);display:inline-block}

.bottombar{left:0;top:3227px;width:1200px;height:83px;font-family:'Roboto',sans-serif;color:var(--link);font-size:16px;font-weight:500}
.bottombar .brand-sm{position:absolute;left:73px;top:28px}
</style>
</head>
<body>

<div class="abs topbar">
  <div class="notice">The fund will go to the poor... <span>Donate Now</span></div>
  <div class="follow">Follow us: <i class="dot"></i><i class="dot"></i><i class="dot"></i><i class="dot"></i></div>
</div>

<header class="abs nav">
  <div class="brand"><span class="wordmark">Velmo Puna</span></div>
  <div class="menu" style="left:328px"><span class="num">01</span><span class="lbl">What We Do ˅</span></div>
  <div class="menu" style="left:459px"><span class="num">02</span><span class="lbl">Benefits</span></div>
  <div class="menu" style="left:542px"><span class="num">03</span><span class="lbl">How Does It Work? ˅</span></div>
  <div class="menu" style="left:712px"><span class="num">04</span><span class="lbl">Contact Us ˅</span></div>
  <div class="menu" style="left:824px"><span class="num">05</span><span class="lbl">Our Mission ˅</span></div>
  <div class="menu" style="left:941px"><span class="num">06</span><span class="lbl">Contact</span></div>
  <div class="search"><svg width="12" height="12" viewBox="0 0 12 12"><circle cx="5" cy="5" r="3.5" fill="none" stroke="#2b2d5b" stroke-width="1.5"/><line x1="7.5" y1="7.5" x2="10.5" y2="10.5" stroke="#2b2d5b" stroke-width="1.5"/></svg></div>
</header>

<section class="abs hero" role="img" aria-label="Photo of children wrapped in shawls and blankets sitting outdoors">
  <svg class="arrow" style="left:54px" width="12" height="20" viewBox="0 0 12 20"><polyline points="10,2 2,10 10,18" fill="none" stroke="#fff" stroke-width="2"/></svg>
  <svg class="arrow" style="left:1134px" width="12" height="20" viewBox="0 0 12 20"><polyline points="2,2 10,10 2,18" fill="none" stroke="#fff" stroke-width="2"/></svg>
  <h1>Bringing Smiles To Millions!</h1>
  <div class="btn">Donate Now</div>
</section>

<h2 class="abs section-title">Our Mission</h2>

<div class="abs framed" style="left:126px;top:998px;width:450px;height:354px" role="img" aria-label="Pile of old mobile phones"></div>
<p class="abs copy" style="left:645px;top:1045px">There are thousands of mobiles lying around in offices around Australia.  The IT department tend to be at a loss of what to do with them.   Most just get taken by the eco-waste collections.  Velmo Puna offers a solution to pay for the recycle and give the proceeds to Social Good.  Now that back room full of used technology, is your company’s pathway to social good.</p>

<p class="abs copy" style="left:126px;top:1478px">Velmo Puna can give you peace of mind, by repurposing or recycling mobiles.  This extends the life of a phone, and gives it a new lease of life.  We only take phones that a suitable for re-use, and suggest those cannot be, are collected by eco-waste collections.  These are sustainable practices that we ensure are doing right by the environment.</p>
<div class="abs framed" style="left:660px;top:1431px;width:450px;height:354px;background:linear-gradient(180deg,#fff 0%,#e8f3e6 40%,#6cc05a 70%,#fff 100%)" role="img" aria-label="Smartphones piled in a green recycling bin"></div>

<div class="abs photo" style="left:126px;top:1865px;width:450px;height:353px;background:linear-gradient(160deg,#7d9a4e 0%,#3a3a3a 35%,#d9dde0 60%,#9a2f22 100%)" role="img" aria-label="Stack of used smartphones and a tablet on a red surface"></div>
<p class="abs copy" style="left:645px;top:1947px">This is a win/win all round.  Organisations can donate proceeds of unused mobiles to charity, and someone else get access to an affordable working mobile phone.  By following sustainable recycling practices and extending life of a mobile through reuse, the environmental impact is minimised.</p>

<p class="abs copy" style="left:126px;top:2343px">Furthermore, in order to create and sustain a better future, Velmo Puna works closely with students and younger generations, specifically Generation Zs.  Not only do we teach these exceptional young people vital business skills, by educating them about the structure of organisations, we also plant the seeds of philanthropy within them.  Helping them become the compassionate leader that our future needs</p>
<div class="abs photo" style="left:660px;top:2277px;width:450px;height:354px;background:linear-gradient(180deg,#cfd6d3 0%,#8a8478 45%,#6a5b52 75%,#a19a90 100%)" role="img" aria-label="Students working together at desks in a classroom"></div>

<p class="abs closing">Our hope, is that we can all work together to become agents of social good.  Leaving our world a little better than what it was yesterday.</p>

<footer class="abs footer">
  <div class="col contact" style="left:73px">
    <h3>Contact Info</h3>
    <div class="lab"><svg width="10" height="14" viewBox="0 0 10 14"><path d="M5 0a5 5 0 0 1 5 5c0 4-5 9-5 9S0 9 0 5a5 5 0 0 1 5-5z" fill="#f06b3a"/><circle cx="5" cy="5" r="2" fill="#8eaeb6"/></svg>LOCATION</div>
    <div class="val">48 Orrin Lane, Maple Cove<br>Harbour, Canada</div>
    <div class="lab"><svg width="14" height="14" viewBox="0 0 14 14"><path d="M3 1l3 3-2 2c1 2 2 3 4 4l2-2 3 3-2 2C6 13 1 8 1 3z" fill="none" stroke="#f06b3a" stroke-width="1.3"/></svg>CALL US</div>
    <div class="val">555-0142-0199</div>
    <div class="lab"><svg width="14" height="10" viewBox="0 0 14 10"><rect width="14" height="10" fill="#f06b3a"/><polyline points="0,0 7,6 14,0" fill="none" stroke="#8eaeb6" stroke-width="1.3"/></svg>EMAIL US</div>
    <div class="val">hello@velmopuna.org</div>
  </div>
  <div class="col" style="left:344px">
    <h3>Our Support</h3>
    <ul><li>Private Policies</li><li>Donate Now</li><li>Become A Volunteer</li><li>Careers</li><li>Contact Us</li><li>Paid Programs</li><li>Partnership</li></ul>
  </div>
  <div class="col" style="left:615px">
    <h3>Our Services</h3>
    <ul><li>Donate</li><li>Sponsor</li><li>Fundraise</li><li>Volunteer</li><li>Partner</li><li>Jobs</li><li>Form</li></ul>
  </div>
  <div class="col" style="left:797px;width:330px">
    <h3>Recent News</h3>
    <div class="news">
      <div class="thumb" style="background:linear-gradient(135deg,#c9a06a,#b8463c)" role="img" aria-label="Children in a poor neighbourhood"></div>
      <div class="txt">Support About Poverty To Poor Family<div class="meta"><i></i>Poor, 22 January</div></div>
    </div>
    <div class="news">
      <div class="thumb" style="background:linear-gradient(135deg,#7a8a9a,#a0684a)" role="img" aria-label="Young schoolboy portrait"></div>
      <div class="txt">Mostly Suffered School Boys Care<div class="meta"><i></i>Health, 24 February</div></div>
    </div>
  </div>
</footer>

<div class="abs bottombar">
  <div class="brand-sm"><span class="wordmark">Velmo Puna</span></div>
  <div style="position:absolute;left:460px;top:32px">2020 Velmo Puna . All Rights Reserved</div>
  <div style="position:absolute;left:882px;top:32px">Terms &amp; Conditions Privacy Policy</div>
</div>

</body>
</html>
```